Healthcare recruitment agency - Brochure Design Project

We are looking to develop a new brochure for our business. Rather than a brochure we will actually have 4 x A4 double sided flyers.
Each flyer will have the same content on front side and sector specific content on the back page.
The sectors will be:
a. Homelessness & Substance Misuse
b. Elderly Care
c. Learning Disabilities
d. Mental Health
It is important for us to get the base design right as this will follow suit across all our communications, the winning designer will get more work including mouse mat, folder and further flyers.
We are a people orientated business for both our staff and the people who they care for, imagery is important and we will source the final images (a couple attached to start things rolling).
I also like the idea of a people montage (see eye montage for an idea of what i mean) This could help describe the varied healthcare element of what we do and extend to other marketing materials with the relevant image highlighted from the rest.
Initially focus on 1 x double sided A4 flyer so we can get the design right, then we can go from there! Also attached is some copy to add to the initial flyer to help the concept develop.
Once the base design has been agreed, images and copy will be sent for the other x3 flyers to make up the equivalent of an 8pp brochure, although x4 pages will be identical.
The first page is generic about the company
The second page is on 'homeless and substance misuse' support staff.
Update: I have just added a file (velo logo) this is the group logo that should be on the front page somewhere. Plus a AI version of the Tarsk logo.
Updates
Hi Guys,
Target Market(s)
Healthcare and social care market, care managers, senior healthcare buyers
Industry/Entity Type
Healthcare
Requirements
Must have
- Our logo and group logo
Use our colours of green, grey and plum (in that order)

```html
<!DOCTYPE html>
<html lang="en">
<head>
<meta charset="utf-8">
<title>Tarsk – Homelessness &amp; Substance Misuse</title>
<link href="https://fonts.googleapis.com/css2?family=Source+Sans+3:wght@400;600;700&display=swap" rel="stylesheet">
<style>
  :root {
    --green: #9fd26b;
    --green-title: #8cc63e;
    --grey: #7b8ea0;
    --plum: #9a2fd6;
    --page: #ececec;
    --header-top: #d9e4ea;
    --header-bottom: #e9eef1;
    --white: #ffffff;
  }
  * { box-sizing: border-box; margin: 0; padding: 0; }
  html, body { width: 905px; height: 1200px; overflow: hidden; }
  body {
    font-family: "Source Sans 3", sans-serif;
    background: radial-gradient(ellipse at 55% 35%, #fbfbfb 0%, var(--page) 70%, #dedede 100%);
    position: relative;
  }
  .flyer-header {
    position: absolute; left: 0; top: 0; width: 905px; height: 130px;
    background: linear-gradient(180deg, var(--header-top), var(--header-bottom));
    border-bottom: 2px dotted #b9c9d3;
  }
  .sector-title {
    position: absolute; left: 32px; top: 36px; width: 621px; height: 72px;
    border: 1px solid #a9b3b8; border-radius: 18px;
    background: linear-gradient(180deg, #eef1f2, #dfe4e6);
    color: var(--green-title);
    font-weight: 700; font-size: 34px;
    display: flex; align-items: center; padding-left: 14px;
  }
  .key-points {
    position: absolute; left: 38px; top: 164px; width: 800px;
    list-style: none; color: var(--plum); font-size: 28px; line-height: 1.22;
  }
  .key-points li { padding-left: 16px; text-indent: -16px; margin-bottom: 13px; }
  .key-points li::before { content: "• "; }
  .intro-panel {
    position: absolute; left: 24px; top: 423px; width: 864px; height: 488px;
    background: var(--green); border-radius: 16px;
    color: var(--white); padding: 24px 46px 0 18px;
    font-size: 19.5px; line-height: 30px;
  }
  .intro-panel p { margin: 0; }
  .intro-panel .lead { font-weight: 700; line-height: 25px; }
  .intro-panel .lead:first-child { margin-bottom: 6px; }
  .intro-panel .closing { margin-top: 8px; }
  .sector-photo {
    position: absolute; left: 304px; top: 827px; width: 580px; height: 349px;
    border: 6px solid var(--green); border-radius: 14px;
    background: linear-gradient(160deg, #5d6d6e 0%, #2e3a3b 35%, #8e9c9a 65%, #c9d2cf 100%);
  }
  .brand-name {
    position: absolute; left: 36px; top: 1070px;
    color: var(--plum); font-weight: 600; font-size: 56px; line-height: 1;
  }
</style>
</head>
<body>
  <header class="flyer-header">
    <h1 class="sector-title">Homelessness &amp; Substance Misuse</h1>
  </header>

  <ul class="key-points">
    <li>We currently provide staff to homeless and substance misuse organisations</li>
    <li>Tarsk have experienced and fully compliant staff ready to work now across London</li>
    <li>Bespoke training provided on request</li>
    <li>Swedish Derogation staff available</li>
  </ul>

  <section class="intro-panel">
    <p class="lead">We are a leading supplier of support / project workers and key workers to a number of London's homeless and substance misuse organisations.</p>
    <p>We are fully aware that the role within this specific area is varied, requiring an interactive person who is happy to get involved. ‘Support Worker’ has such a varied meaning and not all support workers are suitable to this type of work, we work hard to ensure that relevant staff are trained in-house to assess their suitability.</p>
    <p>As a new client the first element that you would expect is that one of our Account Managers will visit each of your services or projects to gain a full understanding the levels of support that are required and prepare this information so staff are completely briefed before they attend.</p>
    <p class="lead closing">Our staff will have experience of working alongside the homeless and drug and alcohol misuse or have relevant transferable skills and experience to ensure you get great supplements to your team.</p>
  </section>

  <div class="sector-photo" role="img" aria-label="Photograph of a homeless person lying on a pavement beneath a window, in muted teal-grey tones"></div>

  <div class="brand-name">Tarsk</div>
</body>
</html>
```